emerald card

Belvardi/Gems
Est.1972
We are a direct Importer of Colombian Emeralds, with gem lab certificates KSR,PMB 1.0ct. and over.Gem ID and Country of origin
Hal Belvardi belvo@postwing.example
469 555 0176 www. belvardiline.example
The current web page is being redesigned,please ,Belvardi/Gems is a new company. We specialize in Colombian Emeralds.
Some of the designers used the existing web page and companies and created business cards for the wrong companies.
The blue back ground deign from Sri Lanka is the only card design that has all the correct information.

Target Market(s)

Fine Jewelry

Industry/Entity Type

Business

Contact Information for Business Card

Belvardi/Gems

Font styles to use
Other font styles liked:
• Roman

Requirements
Must have
• Belvardi/Gems Hal Belvardi
P.O.Box 318270 Dallas,Tx.75908 Ph. 469 555 0176 E-Mail:belvo@postwing.example
www.belvardiline.example, Emeralds over 1.0ct. are certified for Country of origin and Gem ID-KSR or PMB cerificates.

We are importers of Colombian Emeralds all Emeralds over 1.0ct.
Dallas,Tx. 75908
KSR,PMB
Nice to have
• Picture of Emerald
Should not have
• No other company names
We are changing information on our web site.do not use the web page for design.

```html
<!DOCTYPE html>
<html lang="en">
<head>
<meta charset="utf-8">
<title>Belvardi/Gems – Business Card</title>
<link href="https://fonts.googleapis.com/css2?family=Marcellus&family=Open+Sans:wght@400;700&display=swap" rel="stylesheet">
<style>
  :root {
    --backdrop: #ece8e4;
    --crimson: #8c1027;
    --rose: #b8435f;
    --wine-dark: #1c0d10;
    --gold: #d6aa3c;
    --paper: #ffffff;
    --name-red: #6e0f1c;
    --ink: #7a1a22;
    --emerald-light: #a9cdb0;
    --emerald-mid: #6fa07c;
    --emerald-deep: #3f6f4e;
  }
  * { box-sizing: border-box; margin: 0; padding: 0; }
  html, body { width: 1200px; height: 913px; overflow: hidden; }
  body { background: var(--backdrop); position: relative; font-family: "Open Sans", sans-serif; }

  .card {
    position: absolute;
    width: 560px;
    height: 320px;
    overflow: hidden;
    box-shadow: 0 10px 28px rgba(0,0,0,.22);
  }
  .card--front { left: 30px; top: 160px;
    background:
      linear-gradient(180deg, rgba(184,67,95,.75) 0%, rgba(184,67,95,0) 45%),
      linear-gradient(100deg, var(--crimson) 0%, #4a0f1a 45%, var(--wine-dark) 100%);
  }
  .card--back { left: 610px; top: 410px; background: var(--paper); }

  .brand {
    position: absolute;
    left: 0; right: 0;
    text-align: center;
    font-family: "Marcellus", serif;
    color: var(--gold);
    white-space: nowrap;
  }
  .card--front .brand { top: 132px; font-size: 46px; }
  .brand-mark {
    display: block;
    width: 14px; height: 14px;
    border-radius: 50%;
    background: var(--gold);
    margin: 0 auto 10px;
  }
  .brand-rule {
    display: block;
    width: 120px; height: 1px;
    margin: 0 auto 8px;
    background: var(--gold);
    opacity: .6;
  }

  .back-band {
    position: absolute;
    left: 0; top: 0; right: 0; height: 132px;
    background:
      linear-gradient(180deg, rgba(184,67,95,.8) 0%, rgba(184,67,95,0) 60%),
      linear-gradient(100deg, var(--crimson) 0%, #4a0f1a 55%, var(--wine-dark) 100%);
  }
  .back-band .brand { top: 30px; font-size: 38px; }
  .back-band .brand-mark { width: 12px; height: 12px; margin-bottom: 6px; }

  .emerald-photo {
    position: absolute;
    left: 28px; top: 148px;
    width: 124px; height: 108px;
    border-radius: 14px;
    background: radial-gradient(circle at 40% 35%, var(--emerald-light), var(--emerald-mid) 55%, var(--emerald-deep));
    opacity: .85;
  }
  .person { position: absolute; left: 166px; top: 184px; }
  .person-name { font-weight: 700; font-size: 17px; color: var(--name-red); white-space: nowrap; }
  .person-role { font-size: 12px; color: var(--ink); white-space: nowrap; }

  .contacts {
    position: absolute;
    left: 310px; top: 146px;
    list-style: none;
    font-size: 12.5px;
    color: var(--ink);
  }
  .contacts li { display: flex; align-items: center; gap: 9px; height: 24px; white-space: nowrap; }
  .contacts svg { width: 14px; height: 14px; fill: var(--ink); flex: none; }

  .specialty {
    position: absolute;
    left: 20px; right: 20px; top: 272px;
    text-align: center;
    font-size: 11px;
    line-height: 15px;
    color: var(--ink);
  }

  .back-edge {
    position: absolute; left: 0; right: 0; bottom: 0; height: 6px;
    background: var(--crimson);
  }
</style>
</head>
<body>

<section class="card card--front" aria-label="Card front">
  <div class="brand">
    <span class="brand-mark"></span>
    <span class="brand-rule"></span>
    Belvardi/Gems
  </div>
</section>

<section class="card card--back" aria-label="Card back">
  <div class="back-band">
    <div class="brand">
      <span class="brand-mark"></span>
      <span class="brand-rule"></span>
      Belvardi/Gems
    </div>
  </div>

  <div class="emerald-photo" role="img" aria-label="Photo of a cut emerald gemstone"></div>

  <div class="person">
    <p class="person-name">Hal Belvardi</p>
    <p class="person-role">Owner / Propritor</p>
  </div>

  <ul class="contacts">
    <li>
      <svg viewBox="0 0 24 24" aria-hidden="true"><path d="M6.6 10.8a15.1 15.1 0 0 0 6.6 6.6l2.2-2.2a1 1 0 0 1 1-.25 11.4 11.4 0 0 0 3.6.57 1 1 0 0 1 1 1V20a1 1 0 0 1-1 1A17 17 0 0 1 3 4a1 1 0 0 1 1-1h3.5a1 1 0 0 1 1 1c0 1.25.2 2.45.57 3.57a1 1 0 0 1-.25 1z"/></svg>
      469 555 0176
    </li>
    <li>
      <svg viewBox="0 0 24 24" aria-hidden="true"><path d="M2 5h20v14H2z M3 6l9 7 9-7" fill="none" stroke="#7a1a22" stroke-width="2"/></svg>
      belvo@postwing.example
    </li>
    <li>
      <svg viewBox="0 0 24 24" aria-hidden="true"><circle cx="12" cy="12" r="9" fill="none" stroke="#7a1a22" stroke-width="2"/><path d="M3 12h18M12 3c3 3 3 15 0 18M12 3c-3 3-3 15 0 18" fill="none" stroke="#7a1a22" stroke-width="1.6"/></svg>
      www.belvardiline.example
    </li>
    <li>
      <svg viewBox="0 0 24 24" aria-hidden="true"><path d="M12 2a7 7 0 0 0-7 7c0 5 7 13 7 13s7-8 7-13a7 7 0 0 0-7-7zm0 9.5A2.5 2.5 0 1 1 12 6.5a2.5 2.5 0 0 1 0 5z"/></svg>
      P.O.Box 318270 Dallas, Tx. 75908
    </li>
  </ul>

  <p class="specialty">Importers of Colombian Emeralds · All emeralds over 1.0ct. certified<br>for Country of origin and Gem ID – KSR or PMB certificates</p>

  <div class="back-edge"></div>
</section>

</body>
</html>
```